celebrating year in businss

aug 22 2014 we will have our 20th anniversary and a grand opening BBQ at our newly purchased building.

we will be celebrating our anniversary
celebrating our new purchase and grand opening
honoring our customers, friends and family
everyone is invited

```html
<!DOCTYPE html>
<html lang="en">
<head>
<meta charset="utf-8">
<title>20th Anniversary &amp; Grand Opening BBQ</title>
<link rel="stylesheet" href="https://fonts.googleapis.com/css2?family=PT+Sans+Narrow:wght@400;700&family=Lobster&family=Alfa+Slab+One&family=Comic+Neue:wght@700&family=Kaushan+Script&display=swap">
<style>
  :root {
    --red: #e01f26;
    --deep-red: #b3121a;
    --cream: #f7ecc4;
    --sand: #e9d59a;
    --ink: #111111;
    --white: #ffffff;
    --paper: #fdfaf3;
  }
  html, body {
    margin: 0;
    padding: 0;
    width: 910px;
    height: 1200px;
    overflow: hidden;
    background: var(--paper);
  }
  .poster {
    position: relative;
    width: 910px;
    height: 1200px;
    overflow: hidden;
    background: linear-gradient(180deg, #fffefb 0%, #fbf3e0 60%, #f9eee0 100%);
    font-family: "PT Sans Narrow", sans-serif;
  }
  .backdrop { position: absolute; inset: 0; }

  .header {
    position: absolute;
    left: 0; top: 33px;
    width: 100%; height: 97px;
    border-top: 2px solid var(--red);
    border-bottom: 2px solid var(--red);
    box-sizing: border-box;
  }
  .brand {
    position: absolute;
    left: 74px; top: 57px;
    display: flex; align-items: center; gap: 14px;
  }
  .brand-mark {
    width: 34px; height: 34px;
    border-radius: 50%;
    background: var(--red);
  }
  .brand-name {
    font-family: "PT Sans Narrow", sans-serif;
    font-weight: 700;
    font-size: 44px;
    color: var(--deep-red);
    letter-spacing: 1px;
    line-height: 1;
  }

  .ribbon-photo {
    position: absolute;
    left: 479px; top: 65px;
    width: 431px; height: 613px;
    background: radial-gradient(ellipse at 55% 45%, #c2242c 0%, #d9a09a 35%, rgba(250,240,232,0.6) 62%, rgba(255,255,255,0) 78%);
  }

  .date {
    position: absolute;
    left: 71px; top: 172px;
    margin: 0;
    font-weight: 700;
    font-size: 56px;
    color: var(--ink);
    line-height: 1;
    letter-spacing: 0.5px;
  }
  .date .day { font-size: 70px; }

  .years {
    position: absolute;
    left: 58px; top: 236px;
    font-family: "Alfa Slab One", serif;
    font-size: 250px;
    line-height: 1;
    color: #f2a23a;
    -webkit-text-stroke: 6px var(--white);
    paint-order: stroke fill;
    text-shadow: -10px 8px 0 #a8a8a8;
  }
  .years sup {
    font-family: "PT Sans Narrow", sans-serif;
    font-weight: 700;
    font-size: 54px;
    color: var(--deep-red);
    -webkit-text-stroke: 0;
    text-shadow: none;
    vertical-align: top;
    position: relative; top: 32px; left: 4px;
  }
  .anniv-banner {
    position: absolute;
    left: 51px; top: 359px;
    width: 372px; height: 70px;
    text-align: center;
    color: var(--white);
  }
  .anniv-banner .title {
    font-family: "Lobster", sans-serif;
    font-size: 46px;
    line-height: 1;
    padding-top: 6px;
  }
  .anniv-banner .sub {
    font-family: "PT Sans Narrow", sans-serif;
    font-weight: 700;
    font-size: 12px;
    letter-spacing: 9px;
    margin-top: -2px;
  }

  .amp {
    position: absolute;
    left: 452px; top: 410px;
    font-family: "PT Sans Narrow", sans-serif;
    font-weight: 700;
    font-size: 230px;
    line-height: 1;
    color: var(--sand);
    text-shadow: 8px 6px 0 var(--deep-red);
  }

  .grand-opening {
    position: absolute;
    left: 525px; top: 650px;
    transform: rotate(-30deg);
    transform-origin: left top;
    color: var(--red);
    font-weight: 700;
    line-height: 0.9;
  }
  .grand-opening .grand {
    display: block;
    font-size: 46px;
    letter-spacing: 26px;
    color: var(--deep-red);
    padding-left: 6px;
  }
  .grand-opening .opening {
    display: block;
    font-size: 92px;
    letter-spacing: 1px;
  }

  .skewers {
    position: absolute;
    left: 696px; top: 712px;
    width: 90px; height: 152px;
    border-radius: 20px;
    background: linear-gradient(160deg, rgba(17,17,17,0.55), rgba(17,17,17,0.2));
  }

  .grill {
    position: absolute;
    left: 137px; top: 537px;
    width: 330px; height: 422px;
    border-radius: 48% 48% 40% 40%;
    background: radial-gradient(ellipse at 50% 40%, #ea3b35 0%, #e01f26 55%, rgba(224,31,38,0.35) 80%, rgba(224,31,38,0) 100%);
  }
  .bbq {
    position: absolute;
    left: 74px; top: 755px;
    width: 406px; height: 141px;
  }
  .bbq .its {
    position: absolute;
    left: 92px; top: -52px;
    font-family: "Kaushan Script", cursive;
    font-size: 44px;
    color: var(--ink);
  }
  .bbq .word {
    position: absolute;
    left: 80px; top: 28px;
    width: 250px;
    text-align: center;
    font-family: "Alfa Slab One", serif;
    font-size: 62px;
    letter-spacing: 6px;
    color: var(--ink);
    line-height: 1;
  }
  .bbq .time {
    position: absolute;
    left: 300px; top: 124px;
    font-family: "Kaushan Script", cursive;
    font-size: 40px;
    color: var(--ink);
  }

  .message {
    position: absolute;
    left: 0; top: 990px;
    width: 100%;
    margin: 0;
    text-align: center;
    font-family: "Comic Neue", sans-serif;
    font-weight: 700;
    font-size: 33px;
    line-height: 37px;
    color: var(--white);
  }
  .invite {
    position: absolute;
    left: 0; bottom: 0;
    width: 100%; height: 72px;
    background: rgba(150, 20, 24, 0.55);
    display: flex; align-items: center; justify-content: center;
    margin: 0;
    font-weight: 700;
    font-size: 46px;
    letter-spacing: 16px;
    color: var(--white);
  }
</style>
</head>
<body>
  <main class="poster">
    <svg class="backdrop" width="910" height="1200" viewBox="0 0 910 1200" aria-hidden="true">
      <defs>
        <linearGradient id="wave-red" x1="0" y1="0" x2="0" y2="1">
          <stop offset="0" stop-color="#f04a40"/>
          <stop offset="0.5" stop-color="#e01f26"/>
          <stop offset="1" stop-color="#c41820"/>
        </linearGradient>
      </defs>
      <circle class="sun-left" cx="200" cy="330" r="200" fill="#f7ecc4" opacity="0.85"/>
      <circle class="sun-right" cx="725" cy="715" r="275" fill="#f7ecc4" opacity="0.85"/>
      <path class="wave-back" d="M0 870 C 250 880, 560 860, 910 900 L910 1200 L0 1200 Z" fill="#f3a49a" opacity="0.6"/>
      <path class="wave" d="M0 905 C 260 930, 560 930, 910 950 L910 1200 L0 1200 Z" fill="url(#wave-red)"/>
      <path class="wave-line" d="M0 960 C 300 990, 600 975, 910 1000" stroke="#ff8a7a" stroke-width="3" fill="none" opacity="0.6"/>
    </svg>

    <div class="header"></div>
    <div class="brand">
      <span class="brand-mark"></span>
      <span class="brand-name">HARBOR LINE TRANSPORT INC.</span>
    </div>

    <div class="ribbon-photo" role="img" aria-label="Photo of golden scissors cutting a red ceremonial ribbon"></div>

    <h1 class="date">AUG <span class="day">22</span> 2014</h1>

    <div class="years">20<sup>th</sup></div>
    <svg class="anniv-shape" style="position:absolute;left:40px;top:355px" width="400" height="80" viewBox="0 0 400 80" aria-hidden="true">
      <polygon points="0,12 395,4 388,72 6,78" fill="#e01f26"/>
    </svg>
    <div class="anniv-banner">
      <div class="title">Anniversary</div>
      <div class="sub">CELEBRATION</div>
    </div>

    <div class="amp">&amp;</div>

    <div class="grand-opening">
      <span class="grand">GRAND</span>
      <span class="opening">OPENING</span>
    </div>

    <div class="skewers" role="img" aria-label="Illustration of two grilled kebab skewers"></div>

    <div class="grill" role="img" aria-label="Illustration of a red kettle barbecue grill with flames"></div>
    <div class="bbq">
      <svg width="406" height="141" viewBox="0 0 406 141" aria-hidden="true">
        <polygon points="0,40 60,30 60,120 20,128 35,85" fill="#111"/>
        <polygon points="406,10 346,18 346,110 392,100 378,58" fill="#111"/>
        <polygon points="55,18 350,0 350,110 55,125" fill="#111"/>
        <polygon points="68,28 338,12 338,100 68,113" fill="#fff"/>
      </svg>
      <span class="its">It's</span>
      <span class="word">BBQ</span>
      <span class="time">Time</span>
    </div>

    <p class="message">
      We will be celebrating our anniversary<br>
      celebrating our new purchase and grand opening<br>
      honoring our customers, friends and family
    </p>
    <p class="invite">EVERYONE IS INVITED</p>
  </main>
</body>
</html>
```